Amber Heron Fund Pitch Deck

This is a PowerPoint for use in investor presentations. The copy is written (although it may have small tweaks) and the designer will be responsible for creating a template and some graphical representations inside the presentation.

Note on the logo. Only the Amber Heron should be used, not the text.

```html
<!DOCTYPE html>
<html lang="en">
<head>
<meta charset="utf-8">
<title>Amber Heron Fund Pitch Deck</title>
<link href="https://fonts.googleapis.com/css2?family=Cabin:wght@400;600;700&display=swap" rel="stylesheet">
<style>
:root{
  --page-top:#d4d4d6;
  --page-bottom:#c5c5c7;
  --ink:#262626;
  --body:#3a3a3a;
  --blue:#4a74cf;
  --blue-soft:#6b8fd6;
  --blue-band:#7195d8;
  --blue-deep:#3a64c2;
  --white:#ffffff;
}
*{box-sizing:border-box;margin:0;padding:0}
html,body{width:1200px;height:2652px;overflow:hidden}
body{font-family:"Cabin",sans-serif;color:var(--ink);position:relative;
  background:linear-gradient(var(--page-top) 0 750px,var(--page-bottom) 750px 100%)}
.page-title{position:absolute;left:0;width:1200px;text-align:center;letter-spacing:1px}
.page-title.main{top:70px;font-size:25px;color:#1e1e1e}
.page-title.sub{top:788px;font-size:20px;color:#555}

/* cover slide */
.cover{position:absolute;left:336px;top:250px;width:528px;height:300px;background:#f4f4f5;overflow:hidden;box-shadow:0 14px 24px rgba(0,0,0,.18)}
.cover-photo{position:absolute;left:0;top:0;width:528px;height:240px;background:linear-gradient(160deg,#c9d3df,#8fa1b8 55%,#6f86ad)}
.cover-curve{position:absolute;left:0;top:160px}
.cover-title{position:absolute;top:218px;width:100%;text-align:center;font-size:22px;font-weight:700;letter-spacing:1px}
.cover-url{position:absolute;top:246px;width:100%;text-align:center;font-size:12px;letter-spacing:1.5px;color:#333}
.cover-url::before,.cover-url::after{content:"";display:inline-block;width:26px;height:1px;background:#555;vertical-align:middle;margin:0 8px}
.cover-band{position:absolute;left:0;bottom:0;width:100%;height:6px;background:var(--blue-band)}

/* content slides */
.slide{position:absolute;width:528px;height:296px;overflow:hidden;
  background:linear-gradient(135deg,#ffffff 0%,#f3f3f4 50%,#e2e2e4 100%);
  box-shadow:0 14px 22px rgba(0,0,0,.22)}
.s1{left:46px;top:862px}.s2{left:616px;top:862px}
.s3{left:46px;top:1200px}.s4{left:616px;top:1200px}
.s5{left:46px;top:1552px}.s6{left:616px;top:1552px}
.s7{left:46px;top:1896px}.s8{left:616px;top:1896px}
.s9{left:46px;top:2240px}.s10{left:616px;top:2240px}
.slide-head{position:absolute;left:18px;top:20px;font-size:17px;font-weight:700;padding-left:6px;border-left:2px solid var(--blue);line-height:19px}
.slide-foot{position:absolute;left:0;bottom:0;width:100%;height:28px;background:linear-gradient(var(--blue-band) 0 18px,var(--blue-soft) 18px)}
.foot-num{position:absolute;left:22px;bottom:3px;font-size:6px;color:var(--white)}
.foot-brand{position:absolute;right:22px;top:4px;font-size:7px;color:var(--white);font-weight:600}
.foot-brand span{font-weight:600;margin-right:8px}
.sec{position:absolute;font-size:9px;color:var(--blue);font-weight:600}
.txt{position:absolute;font-size:5.4px;line-height:7.4px;color:var(--body)}
.txt p{margin-bottom:5px}
.txt ul{list-style:none}
.txt li{position:relative;padding-left:8px;margin-bottom:2.5px}
.txt li::before{content:"";position:absolute;left:1px;top:3px;width:2px;height:2px;border-radius:50%;background:var(--body)}
.portrait{position:absolute;background:linear-gradient(180deg,#e7e7e8,#bdbdbf)}
.person-name{position:absolute;font-size:6.2px;color:var(--blue);font-weight:600}
.person-name b{color:var(--blue-deep)}
.rule{position:absolute;height:1px;background:#c9c9cc}
.visual{position:absolute;border-radius:4px}

/* slide 1 */
.hero-name{position:absolute;left:256px;top:116px;font-size:25px;font-weight:700;color:var(--blue)}
.hero-role{position:absolute;left:257px;top:148px;font-size:9.5px;color:#333}

/* market */
.stat{position:absolute;font-size:10.5px;line-height:12px;color:#333}
.stat b{font-size:16px;color:var(--blue);font-weight:700}
.stat-divider{position:absolute;width:1px;height:34px;background:#888}
.source{position:absolute;left:20px;top:177px;width:494px;height:18px;border-radius:9px;background:var(--blue-soft);color:var(--white);font-size:11px;line-height:18px;padding-left:10px}
.source b{font-weight:600}

/* process */
.proc-head{position:absolute;left:16px;top:89px;width:495px;height:19px;display:flex}
.proc-head div{flex:1;color:var(--white);font-size:11px;font-weight:700;text-align:center;line-height:19px}
.proc-line{position:absolute;width:1px;background:var(--blue-soft)}
.proc-box{position:absolute;width:66px;border-radius:4px;color:var(--white);font-size:5px;line-height:6.4px;text-align:center;padding:20px 3px 0}
.proc-icon{position:absolute;left:50%;top:-10px;margin-left:-10px;width:20px;height:20px;border-radius:50%;background:var(--white);border:1.5px solid var(--blue-deep)}
.proc-icon::after{content:"";position:absolute;left:5px;top:5px;width:7px;height:7px;border:1.2px solid var(--blue-deep);border-radius:1px}

/* example */
.ex-row{position:absolute;height:38px;display:flex;color:var(--white)}
.ex-letter{width:28px;background:#5b7fd2;font-size:13px;font-weight:700;display:flex;align-items:center;justify-content:center}
.ex-bar{width:198px;background:var(--blue);font-size:5.6px;line-height:7px;padding:0 10px;display:flex;align-items:center}
.ex-row.right .ex-bar{width:194px;background:#5b83da;text-align:right;justify-content:flex-end}
.ex-word{position:absolute;left:238px;top:164px;transform:rotate(-90deg);transform-origin:center;font-size:31px;font-weight:600;color:var(--blue);letter-spacing:2px;width:160px;text-align:center;margin-left:-80px;margin-top:-18px}

/* customers / fund */
.cust{position:absolute;font-size:10px;line-height:15px;color:#222}
.cust b{font-size:15px;color:var(--blue);font-weight:700}
.cust-rule{position:absolute;width:1px;height:32px;background:#888}
.big{position:absolute;font-size:21px;font-weight:700;color:var(--blue)}
.cap{position:absolute;font-size:7.2px;color:#333}
</style>
</head>
<body>

<div class="page-title main">POWERPOINT TEMPLATE</div>

<section class="cover">
  <div class="cover-photo" role="img" aria-label="Photo of a presenter speaking to colleagues in a bright office meeting room"></div>
  <svg class="cover-curve" width="528" height="90" viewBox="0 0 528 90" aria-hidden="true">
    <path d="M0 70 C120 70 170 30 264 30 C360 30 410 70 528 60 L528 90 L0 90 Z" fill="#f4f4f5"/>
  </svg>
  <div class="cover-title">PRESENTATION TITLE</div>
  <div class="cover-url">www.websiteurl.com</div>
  <div class="cover-band"></div>
</section>

<div class="page-title sub">CLICK ZOOM TO SEE DETAILS</div>

<!-- 01 -->
<section class="slide s1">
  <h2 class="slide-head">AMBER HERON NPL FUND</h2>
  <div class="portrait" style="left:24px;top:58px;width:207px;height:202px" role="img" aria-label="Portrait placeholder for the managing partner"></div>
  <div class="hero-name">GRANT WHITFIELD</div>
  <div class="hero-role">Managing Partner, Investment Committee</div>
  <div class="txt" style="left:250px;top:174px;width:256px">
    <ul>
      <li>More than 20 years of banking experience with Carver Lynde, Union Harbor Bank and NorthRidge Bank</li>
      <li>Director of Pellam Capital Management, in less than 5 years, achieved 4x AUM and outsized returns managing distressed asset fund. Developed framework for additional funds.</li>
      <li>CEO of Tealpine.</li>
    </ul>
  </div>
  <div class="slide-foot"><span class="foot-num">01</span><span class="foot-brand"><span>Amber Heron</span>www.websiteurl.com</span></div>
</section>

<!-- 02 -->
<section class="slide s2">
  <h2 class="slide-head">AMBER HERON NPL FUND</h2>
  <div class="sec" style="left:22px;top:56px">02. The Thesis</div>
  <div class="txt" style="left:22px;top:73px;width:490px">
    <p>Interest rate pressures are designed to break the runaway inflation in real estate prices and bring down employment and wage levels</p>
    <ul>
      <li>Real estate prices have already been impacted.</li>
      <li>Unemployment will increase - and it will be stubborn. There will be no immediate relief to business' internal inflationary pressures.</li>
      <li>A down credit cycle, which hasn't been seen in 15 years, will leave smaller lenders unable to cope with non-performing loans.</li>
      <li>We are in a superior position to support these lenders with personnel and technology to special service these portfolios.</li>
    </ul>
  </div>
  <div class="sec" style="left:22px;top:158px">03. The Edge</div>
  <div class="txt" style="left:22px;top:176px;width:490px">
    <p>Experience with fund management and asset disposal. Utilizing the clues and hints that borrowers and guarantors leave on the Internet, we can special service assets and collect on them more quickly and maximize return.</p>
    <p>Much of the technology and experience as a team can be attributed to the team's experience at Tealpine. The principals were the management team that came on in March 2020 and grew the business from <b>less than 12,000 PPP loans to more than 800,000.</b></p>
  </div>
  <div class="slide-foot"><span class="foot-num">02</span><span class="foot-brand"><span>Amber Heron</span>www.websiteurl.com</span></div>
</section>

<!-- 03 -->
<section class="slide s3">
  <h2 class="slide-head">AMBER HERON NPL FUND</h2>
  <div class="sec" style="left:22px;top:56px">04. The Technology</div>
  <div class="txt" style="left:22px;top:74px;width:490px">
    <p>Most lenders and servicers use LendCore or ServePoint and then software like CollectPro for collections.</p>
    <p>These software packages fail to address the most important factors which is to analyze the borrower (and the guarantors) to allow for customized collection plans. We use enhanced skip tracing developed during PPP forgiveness and collection efforts with advanced social media logic.</p>
    <p>Finally, we use evolving algorithms to price and purchase NPL portfolios at the correct price.</p>
  </div>
  <div class="visual" style="left:24px;top:138px;width:482px;height:115px;background:linear-gradient(100deg,#1b2a55,#2d4d92 45%,#4c77c4 70%,#1d2f5e)" role="img" aria-label="Image of hands typing on a laptop with glowing binary code"></div>
  <div class="slide-foot"><span class="foot-num">03</span><span class="foot-brand"><span>Amber Heron</span>www.websiteurl.com</span></div>
</section>

<!-- 04 -->
<section class="slide s4">
  <h2 class="slide-head">AMBER HERON NPL FUND</h2>
  <div class="sec" style="left:22px;top:56px">03. The People</div>
  <div class="portrait" style="left:24px;top:82px;width:64px;height:62px" role="img" aria-label="Portrait placeholder"></div>
  <div class="person-name" style="left:102px;top:84px">Grant Whitfield I Managing Partner, Investment Committee</div>
  <div class="txt" style="left:102px;top:95px;width:410px">
    <ul>
      <li>More than 20 years of banking experience with Carver Lynde, Union Harbor Bank and NorthRidge Bank</li>
      <li>Director of Pellam Capital Management, in less than 5 years, achieved 4x AUM and outsized returns managing distressed asset fund. Developed framework for additional funds.</li>
      <li>CEO of Tealpine.</li>
    </ul>
  </div>
  <div class="rule" style="left:24px;top:159px;width:486px"></div>
  <div class="portrait" style="left:24px;top:173px;width:64px;height:62px" role="img" aria-label="Portrait placeholder"></div>
  <div class="person-name" style="left:102px;top:174px">Leon Marsh I Managing Partner, Investment Committee</div>
  <div class="txt" style="left:102px;top:185px;width:410px">
    <ul>
      <li>Founder of Vantor Law in Scottsdale, Arizona which became the first law firm in the country sold to private non-lawyer investors.</li>
      <li>Extensive experience with large transactions (including leading the largest 2017 Arizona transaction on behalf of a client). Known for liquidation sales inside bankruptcy. Speaker at National Insolvency Institute conference in Las Vegas.</li>
      <li>COO of Webrook, an early web development company that first implemented a commercially successful e-commerce campaign. Developer of Associate software suite for Association and Non-Profit Management.</li>
      <li>General Counsel of Tealpine.</li>
    </ul>
  </div>
  <div class="slide-foot"><span class="foot-num">04</span><span class="foot-brand"><span>Amber Heron</span>www.websiteurl.com</span></div>
</section>

<!-- 05 -->
<section class="slide s5">
  <h2 class="slide-head">AMBER HERON NPL FUND</h2>
  <div class="sec" style="left:22px;top:58px">05. The People</div>
  <div class="portrait" style="left:24px;top:84px;width:65px;height:60px" role="img" aria-label="Portrait placeholder"></div>
  <div class="person-name" style="left:111px;top:84px">Owen Kessler I Director of Credit Analytics</div>
  <div class="txt" style="left:111px;top:96px;width:400px">
    <ul>
      <li>Product and data specialist with more than 15 years technology and startup experience.</li>
      <li>Founded Orvana Communications, which combined email and chat for customer success professionals. Raised $5 million capital and had more than 40,000 users.</li>
      <li>Led advertising products at Linkfield and grew from $7 million to $45 million in revenue over 5 years.</li>
      <li>Advisory Board member with well-known venture capital firm.</li>
      <li>VP, Products, Tealpine.</li>
    </ul>
  </div>
  <div class="rule" style="left:12px;top:166px;width:500px"></div>
  <div class="portrait" style="left:24px;top:183px;width:65px;height:62px" role="img" aria-label="Portrait placeholder"></div>
  <div class="person-name" style="left:111px;top:184px">Paul Dorsey I Chief Operating Officer</div>
  <div class="txt" style="left:111px;top:196px;width:400px">
    <ul>
      <li>Management Consultant at Breyer &amp; Company and Hallam Audit</li>
      <li>Founder of two companies that grew to more than 1,000 employees.</li>
      <li>COO of Tealpine.</li>
    </ul>
  </div>
  <div class="slide-foot"><span class="foot-num">05</span><span class="foot-brand"><span>Amber Heron</span>www.websiteurl.com</span></div>
</section>

<!-- 06 -->
<section class="slide s6">
  <h2 class="slide-head">AMBER HERON NPL FUND</h2>
  <div class="sec" style="left:24px;top:58px">06. The Market</div>
  <div class="stat" style="left:24px;top:94px;width:140px">The commercial lending market size was valued at <b>$8,823.53</b> billion in 2020</div>
  <svg style="position:absolute;left:166px;top:100px" width="52" height="36" viewBox="0 0 52 36" aria-hidden="true">
    <path d="M2 2 L14 2 L28 18 L14 34 L2 34 L16 18 Z" fill="#4a74cf"/>
    <path d="M22 2 L34 2 L48 18 L34 34 L22 34 L36 18 Z" fill="#4a74cf"/>
  </svg>
  <div class="stat" style="left:240px;top:94px;width:130px">Projected to reach <b>$29,379.83</b> billion by 2030</div>
  <div class="stat-divider" style="left:370px;top:97px"></div>
  <div class="stat" style="left:386px;top:94px;width:130px">Growing at a CAGR of <b>13.1%</b> from 2021 to 2030.</div>
  <div class="source"><b>Source:</b> www.marketscoperesearch.com/commercial-lending-market-A11617</div>
  <div class="stat" style="left:24px;top:210px;width:490px;font-size:11px;line-height:13px">The credit cycle is entering into a period of rising interest rates and corresponding defaults. The fund seeks to take advantage of that emerging opportunity.</div>
  <div class="slide-foot"><span class="foot-num">06</span><span class="foot-brand"><span>Amber Heron</span>www.websiteurl.com</span></div>
</section>

<!-- 07 -->
<section class="slide s7">
  <h2 class="slide-head">AMBER HERON NPL FUND</h2>
  <div class="sec" style="left:22px;top:58px">07. Our Process</div>
  <div class="proc-head">
    <div style="background:#3e69c6">A</div><div style="background:#4674cf">B</div><div style="background:#4d7bd4">C</div><div style="background:#5583d9">D</div><div style="background:#5d89dc">E</div><div style="background:#6690df">F</div><div style="background:#6f96e0">G</div>
  </div>
  <div class="proc-line" style="left:51px;top:108px;height:72px"></div>
  <div class="proc-line" style="left:121px;top:108px;height:18px"></div>
  <div class="proc-line" style="left:191px;top:108px;height:72px"></div>
  <div class="proc-line" style="left:263px;top:108px;height:38px"></div>
  <div class="proc-line" style="left:334px;top:108px;height:62px"></div>
  <div class="proc-line" style="left:405px;top:108px;height:10px"></div>
  <div class="proc-line" style="left:476px;top:108px;height:62px"></div>
  <div class="proc-box" style="left:18px;top:190px;height:56px;background:#3e69c6"><span class="proc-icon"></span>Work with our lender customers on their non-performing loan portfolio.</div>
  <div class="proc-box" style="left:88px;top:135px;height:62px;background:#4674cf"><span class="proc-icon"></span>Purchase participation in non-performing loans</div>
  <div class="proc-box" style="left:158px;top:189px;height:62px;background:#4d7bd4"><span class="proc-icon"></span>Provide special servicing in compliance with bank's servicing criteria.</div>
  <div class="proc-box" style="left:230px;top:155px;height:62px;background:#5583d9"><span class="proc-icon"></span>Provide bank access to NPL platform.</div>
  <div class="proc-box" style="left:301px;top:180px;height:62px;background:#5d89dc"><span class="proc-icon"></span>Maintain first right of refusal to purchase loan using proprietary algorithm.</div>
  <div class="proc-box" style="left:372px;top:127px;height:62px;background:#6690df"><span class="proc-icon"></span>Internal servicing standards.</div>
  <div class="proc-box" style="left:443px;top:180px;height:62px;background:#6f96e0"><span class="proc-icon"></span>Liquidation, when necessary.</div>
  <div class="txt" style="left:22px;top:254px;width:360px;font-weight:600">Initially partner with licensed collection agencies to supplement our in-house abilities (and comply with regulatory requirements). Potential to acquire and bring completely in-house.</div>
  <div class="slide-foot"><span class="foot-num">07</span><span class="foot-brand"><span>Amber Heron</span>www.websiteurl.com</span></div>
</section>

<!-- 08 -->
<section class="slide s8">
  <h2 class="slide-head">AMBER HERON NPL FUND</h2>
  <div class="ex-row" style="left:24px;top:83px"><div class="ex-letter">A</div><div class="ex-bar">Lender – Plains Savings of Topeka</div></div>
  <div class="ex-row" style="left:24px;top:125px"><div class="ex-letter">B</div><div class="ex-bar">Has a non-performing loan on a warehouse, $6 million facility, collateral coverage, non-performing for 90 days</div></div>
  <div class="ex-row" style="left:24px;top:165px"><div class="ex-letter">C</div><div class="ex-bar">We purchase 25% participation, for a 35% discount (25% participation for $812,500)</div></div>
  <div class="ex-row" style="left:24px;top:205px"><div class="ex-letter">D</div><div class="ex-bar">We provide special servicing for 90 days, use technology to profile business and guarantor, use targeted approach to collection</div></div>
  <div class="ex-word">EXAMPLE</div>
  <div class="ex-row right" style="left:286px;top:83px"><div class="ex-bar">Assess value, use algorithm to calculate value on Day 75</div><div class="ex-letter">E</div></div>
  <div class="ex-row right" style="left:286px;top:125px"><div class="ex-bar">Determine to purchase on Day 91 the remaining 75%, at what price, if pass on pricing offered in market, utilize information in pricing database to refine algorithm</div><div class="ex-letter">F</div></div>
  <div class="ex-row right" style="left:286px;top:165px"><div class="ex-bar">Workout specialist submits and plan approval within 3 days</div><div class="ex-letter">G</div></div>
  <div class="ex-row right" style="left:286px;top:205px"><div class="ex-bar">Director constantly monitoring portfolio; monthly presentation to Investment Committee, emphasis on efficiency</div><div class="ex-letter">H</div></div>
  <div class="slide-foot"><span class="foot-num">08</span><span class="foot-brand"><span>Amber Heron</span>www.websiteurl.com</span></div>
</section>

<!-- 09 -->
<section class="slide s9">
  <h2 class="slide-head">AMBER HERON NPL FUND</h2>
  <div class="sec" style="left:22px;top:56px">09. Our Customers</div>
  <div class="txt" style="left:22px;top:79px;width:490px;font-size:7px;line-height:9px">Target Market (It would seem we should narrow the target market and also point out any special relationships, people that Grant can source from last experience or otherwise explain why we have a leg up on pipeline.</div>
  <div class="cust" style="left:22px;top:122px">Community Banks:<br>Nearly <b>5,000</b></div>
  <div class="cust-rule" style="left:134px;top:124px"></div>
  <div class="cust" style="left:160px;top:122px">Mid-Market Banks:<br>Approximately <b>4,000</b></div>
  <div class="cust-rule" style="left:304px;top:124px"></div>
  <div class="cust" style="left:328px;top:122px">Non-bank funds, CDFIs, MDIs:<br>More than <b>1,800</b> CDFI's &amp; MDI's</div>
  <div class="sec" style="left:22px;top:184px">10. Management Structure</div>
  <div class="txt" style="left:22px;top:202px;width:490px;font-size:7px;line-height:9px"><b>AMHR Management, LLC to provide management</b> - Identify that this is the same people as above or just eliminate reference.</div>
  <div class="txt" style="left:22px;top:223px;width:490px;font-size:7px;line-height:9px;font-weight:600">Simon Hale, Grant Whitfield and Leon Marsh to serve on Investment Committee</div>
  <div class="slide-foot"><span class="foot-num">09</span><span class="foot-brand"><span>Amber Heron</span>www.websiteurl.com</span></div>
</section>

<!-- 10 -->
<section class="slide s10">
  <h2 class="slide-head">AMBER HERON NPL FUND</h2>
  <div class="sec" style="left:22px;top:56px">11. Waypoint Co-Sponsored Fund</div>
  <div class="txt" style="left:22px;top:76px;width:490px;font-size:6px">
    <ul>
      <li>Utilize Waypoint network, AMHR technology</li>
      <li>Joint LP Investment, Waypoint affiliates / partners to provide additional LP Investment</li>
    </ul>
  </div>
  <div class="txt" style="left:22px;top:102px;width:490px;font-size:8px;line-height:10px;font-weight:600">NPLHeron, LLC to be GP, 80% of carry to AMHR and 20% to Waypoint</div>
  <div class="sec" style="left:22px;top:127px;font-size:8.5px">12. Projected Size of Fund <span style="font-weight:400">– Initially $200 million, up to $1 billion</span></div>
  <div class="big" style="left:22px;top:144px">$100 million</div>
  <div class="cap" style="left:22px;top:172px">Commitment from AMHR from funds due from WPF</div>
  <div class="rule" style="left:22px;top:188px;width:248px;background:#999"></div>
  <div class="big" style="left:22px;top:196px">$100 million</div>
  <div class="cap" style="left:22px;top:224px">Commitment from from Waypoint or its affiliates / network</div>
  <div class="visual" style="left:322px;top:146px;width:182px;height:112px;background:linear-gradient(130deg,#0f1d3d,#1f3f78 55%,#2d5fae)" role="img" aria-label="Image of a hand touching a glowing financial growth chart"></div>
  <div class="slide-foot"><span class="foot-num">10</span><span class="foot-brand"><span>Amber Heron</span>www.websiteurl.com</span></div>
</section>

</body>
</html>
```